Working Capital graphics

Our business advisory firm requires 9 images to be re-created and improved in the branding of our business.

The 9 images have been uploaded below and the colours and branding of the business can be found at the website www.thornwickadvisory.com.au

```html
<!DOCTYPE html>
<html lang="en">
<head>
<meta charset="utf-8">
<title>Working Capital Cycle – Next $100 of Sales Volume</title>
<link href="https://fonts.googleapis.com/css2?family=Poppins:wght@600;700&display=swap" rel="stylesheet">
<style>
  :root {
    --frame: #d6d6d6;
    --paper: #ffffff;
    --ink-navy: #13307a;
    --seg-peach: #fcc286;
    --seg-navy: #0a2049;
    --seg-royal: #0f3580;
    --seg-blue: #1a4fb8;
    --seg-sky: #0db0f2;
    --seg-orange: #fc9528;
    --seg-apricot: #fcaa55;
    --accent: #fc9528;
    --pole: #17b3ef;
    --label: #ffffff;
  }
  html, body {
    margin: 0;
    padding: 0;
    overflow: hidden;
    background: var(--paper);
  }
  .canvas {
    width: 1200px;
    height: 1075px;
    box-sizing: border-box;
    border: 8px solid var(--frame);
    background: var(--paper);
    overflow: hidden;
  }
  .cycle-chart {
    display: block;
    width: 1184px;
    height: 1059px;
    font-family: "Poppins", sans-serif;
  }
  .segment-label {
    fill: var(--label);
    font-size: 22px;
    font-weight: 600;
    text-anchor: middle;
    letter-spacing: 0.3px;
  }
  .milestone {
    fill: var(--ink-navy);
    font-size: 22px;
    font-weight: 600;
    text-anchor: middle;
    letter-spacing: 0.3px;
  }
  .headline {
    fill: var(--accent);
    font-size: 60px;
    font-weight: 700;
    text-anchor: middle;
  }
  .flag-cloth { fill: var(--accent); }
  .flag-pole { stroke: var(--pole); stroke-width: 5; stroke-linecap: butt; }
</style>
</head>
<body>
<div class="canvas">
<svg class="cycle-chart" viewBox="10 10 1495 1337" xmlns="http://www.w3.org/2000/svg" role="img" aria-label="Working capital cycle for the next $100 of sales volume">
  <defs>
    <clipPath id="ring-shape">
      <path clip-rule="evenodd" d="M784 218 a434 434 0 1 1 -0.1 0 Z M784 381 a271 271 0 1 0 0.1 0 Z"/>
    </clipPath>
    <symbol id="milestone-flag" viewBox="0 0 56 66" overflow="visible">
      <line class="flag-pole" x1="2" y1="10" x2="22" y2="64"/>
      <path class="flag-cloth" d="M6 8 Q18 0 30 5 T52 3 L50 24 Q38 28 26 23 T12 30 Z"/>
    </symbol>
  </defs>

  <g class="ring" clip-path="url(#ring-shape)">
    <polygon fill="var(--seg-peach)"   points="784,652 655,412 667,315 577,270 540,250 680,80 740,150 760,218 828,298 776,382"/>
    <polygon fill="var(--seg-navy)"    points="784,652 776,382 828,298 760,218 740,150 1100,120 1180,300 1140,405 1108,502 1010,502"/>
    <polygon fill="var(--seg-royal)"   points="784,652 1010,502 1108,502 1140,405 1180,300 1350,620 1240,860 1160,868 1063,880 1020,790"/>
    <polygon fill="var(--seg-blue)"    points="784,652 1020,790 1063,880 1160,868 1240,860 1150,1250 850,1150 825,1088 760,1012 806,922"/>
    <polygon fill="var(--seg-sky)"     points="784,652 806,922 760,1012 825,1088 850,1150 520,1200 380,900 420,888 455,793 555,800"/>
    <polygon fill="var(--seg-orange)"  points="784,652 555,800 455,793 420,888 380,900 250,650 380,430 412,430 512,420 553,510"/>
    <polygon fill="var(--seg-apricot)" points="784,652 553,510 512,420 412,430 380,430 380,250 540,250 577,270 667,315 655,412"/>
  </g>

  <g class="segment-labels">
    <text class="segment-label" x="736" y="312">$0</text>
    <text class="segment-label" x="951" y="364">COST OF SALES</text>
    <text class="segment-label" x="1134" y="598">OPERATING</text>
    <text class="segment-label" x="1134" y="625">EXPENSES</text>
    <text class="segment-label" x="1121" y="757">FIXED</text>
    <text class="segment-label" x="1121" y="786">COSTS</text>
    <text class="segment-label" x="1027" y="912">TAX</text>
    <text class="segment-label" x="960" y="973">INTEREST</text>
    <text class="segment-label" x="859" y="1024">DIVIDENDS</text>
    <text class="segment-label" x="510" y="875">AR</text>
    <text class="segment-label" x="510" y="904">DAYS</text>
    <text class="segment-label" x="589" y="954">AP</text>
    <text class="segment-label" x="589" y="983">DAYS</text>
    <text class="segment-label" x="701" y="1005">INV</text>
    <text class="segment-label" x="701" y="1035">DAYS</text>
    <text class="segment-label" x="434" y="636">ADDITIONAL</text>
    <text class="segment-label" x="434" y="664">DEBT</text>
    <text class="segment-label" x="559" y="360">CASH</text>
    <text class="segment-label" x="559" y="390">SHORTFALL</text>
  </g>

  <g class="headline-group">
    <text class="headline" x="784" y="650">NEXT $100 OF</text>
    <text class="headline" x="784" y="713">SALES VOLUME</text>
  </g>

  <g class="milestones">
    <text class="milestone" x="781" y="181">REVENUE $0</text>

    <use href="#milestone-flag" x="1310" y="386" width="56" height="66"/>
    <text class="milestone" x="1252" y="408">GROSS</text>
    <text class="milestone" x="1252" y="437">MARGIN</text>
    <text class="milestone" x="1252" y="466">$0</text>

    <use href="#milestone-flag" x="1280" y="851" width="56" height="66"/>
    <text class="milestone" x="1236" y="887">EBIT</text>
    <text class="milestone" x="1236" y="916">$0</text>

    <use href="#milestone-flag" x="684" y="1128" width="56" height="66"/>
    <text class="milestone" x="811" y="1160">RETAINED</text>
    <text class="milestone" x="811" y="1190">INCOME $0</text>

    <use href="#milestone-flag" x="158" y="854" width="56" height="66"/>
    <text class="milestone" x="284" y="855">AFTER</text>
    <text class="milestone" x="284" y="884">WORKING</text>
    <text class="milestone" x="284" y="914">CAPITAL</text>
    <text class="milestone" x="284" y="943">$0</text>

    <use href="#milestone-flag" x="151" y="384" width="56" height="66"/>
    <text class="milestone" x="288" y="394">AFTER</text>
    <text class="milestone" x="288" y="423">ADDITIONAL</text>
    <text class="milestone" x="288" y="452">FUNDING</text>
    <text class="milestone" x="288" y="481">$0</text>
  </g>
</svg>
</div>
</body>
</html>
```